Flyer brol retro depot (4 pages A 4)

FLYER 4 facing A 4 (4 PAGE A 4) 1 / SEE CONDITIONS OF PACKING CONDITIONS PACKING 2 / IDEA OF WHAT I WANT TO PAGES AND CONCEPT (20 PICTURES PER PAGES EXCEPT FOR THE FIRST 3 / FIRST PAGE PUT THE PICTURES ON THE FIRST PAGE AND THE TEXT WHILE KEEPING THE COLOR AND SPIRIT OF THE EXAMPLE PAGE IDENTITY TITLE FROM PAGE 1: BROL RETRO DEPOT Visit our 650 M2 cork showroom (by appointment) 14 rue des tilleuls, 4460 Vorsel, belgium or www.brolretrodepot.com // info@brolretrodepot.com 4 / PAGE 2, 3, 4 PAGE TEMPLATE WITH 20 PRODUCT IN PAGES AS PICTURES IDEA OF PAGE 2.3, 4

Target Market(s)

no one likes vintage between 30 and 80 years

Font styles to use
Serif

Colors
fdf9cf
e667a6
00a990

Requirements
Must have
• the project must resemble and be in the spirit of the file: file 2, file 3 it misses 20 photos of the page 4 that I will send later if I select you a vintage spirit of the year 60 in the usa

```html
<!DOCTYPE html>
<html lang="en">
<head>
<meta charset="utf-8">
<title>Flyer brol retro depot</title>
<link href="https://fonts.googleapis.com/css2?family=Pacifico&family=Oswald:wght@400;500&family=Signika:wght@400;600&display=swap" rel="stylesheet">
<style>
  :root {
    --board: #efefef;
    --teal: #1f9c9c;
    --teal-dark: #157a7c;
    --pink: #e8868b;
    --cream: #ede8dd;
    --paper: #dcd7cc;
    --night: #0e0f1c;
    --ink-grey: #8a8a8a;
    --white: #ffffff;
    --placeholder: #5e5e5e;
  }
  * { box-sizing: border-box; margin: 0; padding: 0; }
  html, body { width: 1054px; height: 1200px; overflow: hidden; background: var(--board); }
  .board { position: relative; width: 1054px; height: 1200px; font-family: "Signika", sans-serif; }

  .board-brand { position: absolute; top: 44px; left: 0; width: 100%; display: flex; justify-content: center; align-items: center; gap: 12px; }
  .brand-dot { width: 26px; height: 26px; border-radius: 50%; background: var(--pink); flex: none; }
  .brand-name { font-family: "Oswald", sans-serif; font-weight: 500; font-size: 34px; letter-spacing: 2px; color: var(--teal); white-space: nowrap; }
  .board-title { position: absolute; top: 128px; width: 100%; text-align: center; font-family: "Pacifico", cursive; font-weight: 400; font-size: 52px; color: var(--teal); line-height: 1; }

  .sheet-label { position: absolute; font-family: "Signika", sans-serif; font-weight: 600; font-size: 18px; color: var(--ink-grey); transform: translateX(-50%); white-space: nowrap; }

  .sheet { position: absolute; width: 301px; height: 424px; overflow: hidden; box-shadow: 0 10px 14px -6px rgba(0,0,0,.35); }

  /* front page */
  .cover { background: var(--night); }
  .cover-top { position: absolute; left: 0; top: 0; width: 100%; height: 70px; }
  .cover-photo { position: absolute; left: 0; top: 46px; width: 100%; height: 260px; }
  .cover-photo.warm {
    background:
      radial-gradient(ellipse 60% 22% at 48% 72%, rgba(236,214,190,.85) 0%, rgba(200,160,128,.5) 45%, rgba(0,0,0,0) 100%),
      radial-gradient(ellipse 70% 30% at 45% 48%, rgba(150,88,56,.9) 0%, rgba(90,52,38,.6) 50%, rgba(0,0,0,0) 100%),
      linear-gradient(180deg, #0d0e18 0%, #181a2a 25%, #2a2230 42%, #3a2a28 62%, #1c1820 85%, #0d0e18 100%);
  }
  .cover-photo.cool {
    background:
      radial-gradient(ellipse 60% 22% at 48% 72%, rgba(196,214,212,.85) 0%, rgba(140,162,164,.5) 45%, rgba(0,0,0,0) 100%),
      radial-gradient(ellipse 70% 30% at 45% 48%, rgba(120,128,126,.9) 0%, rgba(70,78,82,.6) 50%, rgba(0,0,0,0) 100%),
      linear-gradient(180deg, #0d0e18 0%, #161c2a 25%, #222a36 42%, #2c3236 62%, #161a22 85%, #0d0e18 100%);
  }
  .cover-brand { position: absolute; top: 14px; left: 0; width: 100%; display: flex; justify-content: center; align-items: center; gap: 6px; }
  .cover-brand .brand-dot { width: 14px; height: 14px; }
  .cover-brand .brand-name { font-size: 20px; letter-spacing: 1px; }
  .cover-bottom { position: absolute; left: 0; top: 290px; width: 100%; height: 134px; }
  .cover-name { position: absolute; top: 314px; width: 100%; text-align: center; font-family: "Pacifico", cursive; font-weight: 400; font-size: 26px; color: var(--white); line-height: 1.1; }
  .cover-line { position: absolute; width: 100%; text-align: center; font-family: "Oswald", sans-serif; font-size: 11.5px; color: var(--white); letter-spacing: .2px; text-transform: uppercase; white-space: nowrap; }
  .cover-line.showroom { top: 360px; }
  .cover-line.address { top: 380px; }
  .cover-line em { font-style: normal; color: var(--pink); }

  .sheet-footer { position: absolute; left: 0; bottom: 0; width: 100%; height: 21px; background: var(--pink); display: flex; justify-content: center; align-items: center; gap: 8px; color: var(--white); font-family: "Oswald", sans-serif; text-transform: uppercase; white-space: nowrap; }
  .sheet-footer::before { content: ""; position: absolute; left: 0; top: -6px; width: 100%; height: 6px; background: var(--teal-dark); }
  .cover .sheet-footer { font-size: 8.5px; }
  .sheet-footer .dot { width: 7px; height: 7px; border-radius: 50%; border: 1.3px solid var(--white); }
  .sheet-footer .sep { opacity: .8; }

  .phone-tag { position: absolute; left: 20px; top: 252px; width: 98px; height: 60px; background: var(--pink); border-radius: 6px; transform: rotate(-10deg); color: var(--white); text-align: center; font-family: "Oswald", sans-serif; font-size: 11.5px; padding-top: 8px; white-space: nowrap; }
  .phone-tag svg { display: block; margin: 0 auto 3px; }
  .tag-string { position: absolute; }

  /* catalogue page */
  .catalogue { background: var(--paper); }
  .cat-head { position: absolute; left: 0; top: 0; width: 100%; height: 80px; }
  .cat-brand { position: absolute; top: 22px; left: 112px; display: flex; align-items: center; gap: 5px; }
  .cat-brand .brand-dot { width: 12px; height: 12px; }
  .cat-brand .brand-name { font-size: 16px; color: var(--cream); letter-spacing: 1px; }
  .call-tag { position: absolute; left: 24px; top: 22px; width: 70px; height: 44px; background: var(--pink); border-radius: 5px; transform: rotate(-12deg); color: var(--white); font-family: "Oswald", sans-serif; text-align: center; line-height: 1; padding-top: 6px; white-space: nowrap; }
  .call-tag strong { display: block; font-weight: 500; font-size: 18px; }
  .call-tag span { font-size: 7px; }

  .grid { position: absolute; left: 8px; top: 81px; width: 285px; display: grid; grid-template-columns: repeat(5, 57px); grid-auto-rows: 75px; list-style: none; }
  .item { display: flex; flex-direction: column; align-items: center; }
  .thumb { width: 52px; height: 52px; border-radius: 50%; background: var(--c); box-shadow: 0 1px 2px rgba(0,0,0,.3); border: 2px solid var(--white); }
  .item b { margin-top: 4px; font-weight: 600; font-size: 5px; color: var(--teal-dark); white-space: nowrap; }
  .placeholder .thumb { background: var(--placeholder); border: 2px solid #cfcac0; display: flex; flex-direction: column; justify-content: center; align-items: center; color: #a9a9a9; font-family: "Oswald", sans-serif; line-height: 1; }
  .placeholder .thumb strong { font-weight: 500; font-size: 10px; }
  .placeholder .thumb small { font-size: 4.5px; letter-spacing: .5px; }
  .catalogue .sheet-footer { font-size: 5.5px; }
  .catalogue .sheet-footer .dot { width: 5px; height: 5px; border-width: 1px; }
</style>
</head>
<body>
<main class="board">

  <div class="board-brand"><span class="brand-dot"></span><span class="brand-name">BROL RETRO DEPOT</span></div>
  <h1 class="board-title">Flyer brol retro depot</h1>

  <p class="sheet-label" style="left:358px;top:226px">Front Page</p>
  <p class="sheet-label" style="left:692px;top:228px">Front Page (New Version)</p>

  <!-- front page -->
  <section class="sheet cover" style="left:211px;top:258px">
    <div class="cover-photo warm" role="img" aria-label="Night photo of a cream vintage convertible parked in front of a silver trailer diner with a neon sign and a fuel pump, warm tones"></div>
    <svg class="cover-top" viewBox="0 0 301 70" preserveAspectRatio="none" aria-hidden="true"><polygon fill="var(--cream)" points="0,0 301,0 301,52 285,56 270,50 252,58 236,51 218,57 200,50 180,59 162,52 145,57 126,49 108,57 90,52 72,58 55,50 38,56 20,51 0,57"/></svg>
    <div class="cover-brand"><span class="brand-dot"></span><span class="brand-name">BROL RETRO DEPOT</span></div>
    <svg class="cover-bottom" viewBox="0 0 301 134" preserveAspectRatio="none" aria-hidden="true"><polygon fill="var(--teal)" points="0,14 18,8 36,16 55,9 74,15 92,7 110,14 130,8 150,16 170,9 190,15 210,7 230,14 250,8 270,15 288,9 301,12 301,134 0,134"/></svg>
    <svg class="tag-string" style="left:52px;top:236px" width="60" height="26" aria-hidden="true"><path d="M4 24 L32 2 L56 18" fill="none" stroke="#c9b9a0" stroke-width="1"/></svg>
    <div class="phone-tag">
      <svg width="22" height="22" viewBox="0 0 22 22" aria-hidden="true"><circle cx="11" cy="11" r="9.5" fill="none" stroke="#fff" stroke-width="1.6"/><path d="M7.5 6.5c.6-.6 1.3-.5 1.7.1l1 1.5c.3.5.2 1-.2 1.4l-.6.5c.5 1.1 1.4 2 2.5 2.5l.5-.6c.4-.4.9-.5 1.4-.2l1.5 1c.6.4.7 1.1.1 1.7l-.7.7c-.6.6-1.6.7-2.6.3-2.4-1-4.3-2.9-5.3-5.3-.4-1-.3-2 .3-2.6z" fill="#fff"/></svg>
      +32 400 128 306
    </div>
    <h2 class="cover-name">Brol Retro Depot</h2>
    <p class="cover-line showroom">Visit our 650 m 2 showroom <em>( by appointment )</em></p>
    <p class="cover-line address">14 rue des tilleuls, 4460 Vorsel, Belgium</p>
    <footer class="sheet-footer"><span class="dot"></span>www.brolretrodepot.com <span class="sep">|</span><span class="dot"></span>info@brolretrodepot.com</footer>
  </section>

  <!-- front page, new version -->
  <section class="sheet cover" style="left:542px;top:258px">
    <div class="cover-photo cool" role="img" aria-label="Night photo of a pale blue vintage convertible parked in front of a silver trailer diner with a neon sign and a fuel pump, cool tones"></div>
    <svg class="cover-top" viewBox="0 0 301 70" preserveAspectRatio="none" aria-hidden="true"><polygon fill="var(--cream)" points="0,0 301,0 301,52 285,56 270,50 252,58 236,51 218,57 200,50 180,59 162,52 145,57 126,49 108,57 90,52 72,58 55,50 38,56 20,51 0,57"/></svg>
    <div class="cover-brand"><span class="brand-dot"></span><span class="brand-name">BROL RETRO DEPOT</span></div>
    <svg class="cover-bottom" viewBox="0 0 301 134" preserveAspectRatio="none" aria-hidden="true"><polygon fill="var(--teal)" points="0,14 18,8 36,16 55,9 74,15 92,7 110,14 130,8 150,16 170,9 190,15 210,7 230,14 250,8 270,15 288,9 301,12 301,134 0,134"/></svg>
    <svg class="tag-string" style="left:52px;top:236px" width="60" height="26" aria-hidden="true"><path d="M4 24 L32 2 L56 18" fill="none" stroke="#c9b9a0" stroke-width="1"/></svg>
    <div class="phone-tag">
      <svg width="22" height="22" viewBox="0 0 22 22" aria-hidden="true"><circle cx="11" cy="11" r="9.5" fill="none" stroke="#fff" stroke-width="1.6"/><path d="M7.5 6.5c.6-.6 1.3-.5 1.7.1l1 1.5c.3.5.2 1-.2 1.4l-.6.5c.5 1.1 1.4 2 2.5 2.5l.5-.6c.4-.4.9-.5 1.4-.2l1.5 1c.6.4.7 1.1.1 1.7l-.7.7c-.6.6-1.6.7-2.6.3-2.4-1-4.3-2.9-5.3-5.3-.4-1-.3-2 .3-2.6z" fill="#fff"/></svg>
      +32 400 128 306
    </div>
    <h2 class="cover-name">Brol Retro Depot</h2>
    <p class="cover-line showroom">Visit our 650 m 2 showroom <em>( by appointment )</em></p>
    <p class="cover-line address">14 rue des tilleuls, 4460 Vorsel, Belgium</p>
    <footer class="sheet-footer"><span class="dot"></span>www.brolretrodepot.com <span class="sep">|</span><span class="dot"></span>info@brolretrodepot.com</footer>
  </section>

  <!-- catalogue page 1 -->
  <section class="sheet catalogue" style="left:45px;top:715px">
    <svg class="cat-head" viewBox="0 0 301 80" preserveAspectRatio="none" aria-hidden="true"><polygon fill="var(--teal)" points="0,0 301,0 301,60 282,66 264,58 246,67 228,60 208,68 190,59 170,66 150,58 130,67 112,60 92,68 74,59 55,66 36,58 18,66 0,60"/></svg>
    <div class="call-tag"><strong>CALL US</strong><span>+32 400 128 306</span></div>
    <div class="cat-brand"><span class="brand-dot"></span><span class="brand-name">BROL RETRO DEPOT</span></div>
    <ul class="grid">
      <li class="item"><span class="thumb" role="img" aria-label="Railroad crossing sign in a showroom" style="--c:#8a6a4a"></span><b>Rail sign</b></li>
      <li class="item"><span class="thumb" role="img" aria-label="Vintage bar corner" style="--c:#7a5a40"></span><b>Bar corner</b></li>
      <li class="item"><span class="thumb" role="img" aria-label="Garage wall with signs" style="--c:#6d5040"></span><b>Garage wall</b></li>
      <li class="item"><span class="thumb" role="img" aria-label="Old highway road sign" style="--c:#d8d0c0"></span><b>Road sign</b></li>
      <li class="item"><span class="thumb" role="img" aria-label="Round neon fuel sign" style="--c:#c03040"></span><b>Neon disc</b></li>
      <li class="item"><span class="thumb" role="img" aria-label="Yellow car parts neon sign" style="--c:#d8a020"></span><b>Parts sign</b></li>
      <li class="item"><span class="thumb" role="img" aria-label="White round lightbox" style="--c:#e8e4e0"></span><b>Lightbox one</b></li>
      <li class="item"><span class="thumb" role="img" aria-label="Red round lightbox" style="--c:#d03030"></span><b>Lightbox two</b></li>
      <li class="item"><span class="thumb" role="img" aria-label="Blue neon wall clock" style="--c:#2a3a80"></span><b>Wall clock</b></li>
      <li class="item"><span class="thumb" role="img" aria-label="Blue and red neon clock" style="--c:#34408a"></span><b>Round clock</b></li>
      <li class="item"><span class="thumb" role="img" aria-label="Red rimmed neon clock" style="--c:#e8e0e0"></span><b>Red clock</b></li>
      <li class="item"><span class="thumb" role="img" aria-label="Dark neon clock" style="--c:#603030"></span><b>Dark clock</b></li>
      <li class="item"><span class="thumb" role="img" aria-label="Colourful city neon sign" style="--c:#3060a0"></span><b>City neon</b></li>
      <li class="item"><span class="thumb" role="img" aria-label="Mechanic lightbox" style="--c:#f0f0f0"></span><b>Duty lightbox</b></li>
      <li class="item"><span class="thumb" role="img" aria-label="Green coast highway sign" style="--c:#2a5a3a"></span><b>Coast sign</b></li>
      <li class="item"><span class="thumb" role="img" aria-label="Red winged horse neon" style="--c:#e0d8d0"></span><b>Horse neon</b></li>
      <li class="item"><span class="thumb" role="img" aria-label="Blue and red highway neon" style="--c:#2040a0"></span><b>Highway neon</b></li>
      <li class="item"><span class="thumb" role="img" aria-label="Green round neon sign" style="--c:#30a050"></span><b>Sky neon</b></li>
      <li class="item"><span class="thumb" role="img" aria-label="Red star fuel neon" style="--c:#c02020"></span><b>Star neon</b></li>
      <li class="item"><span class="thumb" role="img" aria-label="White and red fuel sign" style="--c:#e8e0e0"></span><b>Junior sign</b></li>
    </ul>
    <footer class="sheet-footer"><span class="dot"></span>www.brolretrodepot.com <span class="sep">|</span><span class="dot"></span>info@brolretrodepot.com</footer>
  </section>

  <!-- catalogue page 2 -->
  <section class="sheet catalogue" style="left:377px;top:715px">
    <svg class="cat-head" viewBox="0 0 301 80" preserveAspectRatio="none" aria-hidden="true"><polygon fill="var(--teal)" points="0,0 301,0 301,60 282,66 264,58 246,67 228,60 208,68 190,59 170,66 150,58 130,67 112,60 92,68 74,59 55,66 36,58 18,66 0,60"/></svg>
    <div class="call-tag"><strong>CALL US</strong><span>+32 400 128 306</span></div>
    <div class="cat-brand"><span class="brand-dot"></span><span class="brand-name">BROL RETRO DEPOT</span></div>
    <ul class="grid">
      <li class="item"><span class="thumb" role="img" aria-label="Round oil lightbox" style="--c:#e6e0dc"></span><b>Oil sign</b></li>
      <li class="item"><span class="thumb" role="img" aria-label="Red traffic warning sign" style="--c:#d02828"></span><b>Warning sign</b></li>
      <li class="item"><span class="thumb" role="img" aria-label="Silver plane model" style="--c:#909090"></span><b>Plane model</b></li>
      <li class="item"><span class="thumb" role="img" aria-label="Life size figure statue" style="--c:#d8d0c8"></span><b>Actor statue</b></li>
      <li class="item"><span class="thumb" role="img" aria-label="Red and white diner bench" style="--c:#d03030"></span><b>Red bench</b></li>
      <li class="item"><span class="thumb" role="img" aria-label="Red diner chair" style="--c:#e4dcd6"></span><b>Red chair</b></li>
      <li class="item"><span class="thumb" role="img" aria-label="Red car trunk chest" style="--c:#b01818"></span><b>Red trunk</b></li>
      <li class="item"><span class="thumb" role="img" aria-label="Black car trunk chest" style="--c:#202020"></span><b>Black trunk</b></li>
      <li class="item"><span class="thumb" role="img" aria-label="Yellow car front wall piece" style="--c:#e0b820"></span><b>Yellow front</b></li>
      <li class="item"><span class="thumb" role="img" aria-label="Black car front wall piece" style="--c:#2a2a2a"></span><b>Black front</b></li>
      <li class="item"><span class="thumb" role="img" aria-label="Red car front wall piece" style="--c:#e8e2de"></span><b>Red front</b></li>
      <li class="item"><span class="thumb" role="img" aria-label="Blue car front wall piece" style="--c:#e4e4e8"></span><b>Blue front</b></li>
      <li class="item"><span class="thumb" role="img" aria-label="Toy rocket statue" style="--c:#ecebec"></span><b>Rocket model</b></li>
      <li class="item"><span class="thumb" role="img" aria-label="Large robot figure" style="--c:#e4e4ea"></span><b>Robot figure</b></li>
      <li class="item"><span class="thumb" role="img" aria-label="Liberty statue replica" style="--c:#eeeeee"></span><b>Liberty statue</b></li>
      <li class="item"><span class="thumb" role="img" aria-label="Astronaut statue" style="--c:#f0f0f0"></span><b>Space statue</b></li>
      <li class="item"><span class="thumb" role="img" aria-label="Top hat figure statue" style="--c:#eeeaea"></span><b>Uncle statue</b></li>
      <li class="item"><span class="thumb" role="img" aria-label="Pin-up figure statue" style="--c:#efeaea"></span><b>Pin-up statue</b></li>
      <li class="item"><span class="thumb" role="img" aria-label="Diner table against brick wall" style="--c:#8a5a48"></span><b>Brick table</b></li>
      <li class="item"><span class="thumb" role="img" aria-label="Black diner table" style="--c:#6a6e72"></span><b>Black table</b></li>
    </ul>
    <footer class="sheet-footer"><span class="dot"></span>www.brolretrodepot.com <span class="sep">|</span><span class="dot"></span>info@brolretrodepot.com</footer>
  </section>

  <!-- catalogue page 3 -->
  <section class="sheet catalogue" style="left:709px;top:715px">
    <svg class="cat-head" viewBox="0 0 301 80" preserveAspectRatio="none" aria-hidden="true"><polygon fill="var(--teal)" points="0,0 301,0 301,60 282,66 264,58 246,67 228,60 208,68 190,59 170,66 150,58 130,67 112,60 92,68 74,59 55,66 36,58 18,66 0,60"/></svg>
    <div class="call-tag"><strong>CALL US</strong><span>+32 400 128 306</span></div>
    <div class="cat-brand"><span class="brand-dot"></span><span class="brand-name">BROL RETRO DEPOT</span></div>
    <ul class="grid">
      <li class="item"><span class="thumb" role="img" aria-label="Red diner table" style="--c:#a02020"></span><b>Red table</b></li>
      <li class="item"><span class="thumb" role="img" aria-label="Red bar stool" style="--c:#e2dcd6"></span><b>Bar stool</b></li>
      <li class="item"><span class="thumb" role="img" aria-label="Red toy convertible" style="--c:#f0eeee"></span><b>Toy car</b></li>
      <li class="item placeholder"><span class="thumb"><strong>IMAGE</strong><small>PLACEHOLDER</small></span><b>Product Name</b></li>
      <li class="item placeholder"><span class="thumb"><strong>IMAGE</strong><small>PLACEHOLDER</small></span><b>Product Name</b></li>
      <li class="item placeholder"><span class="thumb"><strong>IMAGE</strong><small>PLACEHOLDER</small></span><b>Product Name</b></li>
      <li class="item placeholder"><span class="thumb"><strong>IMAGE</strong><small>PLACEHOLDER</small></span><b>Product Name</b></li>
      <li class="item placeholder"><span class="thumb"><strong>IMAGE</strong><small>PLACEHOLDER</small></span><b>Product Name</b></li>
      <li class="item placeholder"><span class="thumb"><strong>IMAGE</strong><small>PLACEHOLDER</small></span><b>Product Name</b></li>
      <li class="item placeholder"><span class="thumb"><strong>IMAGE</strong><small>PLACEHOLDER</small></span><b>Product Name</b></li>
      <li class="item placeholder"><span class="thumb"><strong>IMAGE</strong><small>PLACEHOLDER</small></span><b>Product Name</b></li>
      <li class="item placeholder"><span class="thumb"><strong>IMAGE</strong><small>PLACEHOLDER</small></span><b>Product Name</b></li>
      <li class="item placeholder"><span class="thumb"><strong>IMAGE</strong><small>PLACEHOLDER</small></span><b>Product Name</b></li>
      <li class="item placeholder"><span class="thumb"><strong>IMAGE</strong><small>PLACEHOLDER</small></span><b>Product Name</b></li>
      <li class="item placeholder"><span class="thumb"><strong>IMAGE</strong><small>PLACEHOLDER</small></span><b>Product Name</b></li>
      <li class="item placeholder"><span class="thumb"><strong>IMAGE</strong><small>PLACEHOLDER</small></span><b>Product Name</b></li>
      <li class="item placeholder"><span class="thumb"><strong>IMAGE</strong><small>PLACEHOLDER</small></span><b>Product Name</b></li>
      <li class="item placeholder"><span class="thumb"><strong>IMAGE</strong><small>PLACEHOLDER</small></span><b>Product Name</b></li>
      <li class="item placeholder"><span class="thumb"><strong>IMAGE</strong><small>PLACEHOLDER</small></span><b>Product Name</b></li>
      <li class="item placeholder"><span class="thumb"><strong>IMAGE</strong><small>PLACEHOLDER</small></span><b>Product Name</b></li>
    </ul>
    <footer class="sheet-footer"><span class="dot"></span>www.brolretrodepot.com <span class="sep">|</span><span class="dot"></span>info@brolretrodepot.com</footer>
  </section>

  <p class="sheet-label" style="left:195px;top:1155px">Page 1</p>
  <p class="sheet-label" style="left:527px;top:1155px">Page 2</p>
  <p class="sheet-label" style="left:865px;top:1157px">Page 3</p>

</main>
</body>
</html>
```